Looking for updated Letterhead and Compliments Slips to go with our new updated logo. This stationary will be used for letters to suppliers and customers so needs to be practical while also quite classic.

We are an engineering company so needs to be clean and precise

Target Market(s)

SME'S and large automotive customers

Industry/Entity Type

Automotive

Font styles to use
Sans Serif

Colors
85acd3
0356a4
0792cd
33a6d7
85abd2
ffffff

Requirements
Must have
• Address details as below
• KT Fabrications Limited
• Hallmere Road
• Marrowby
• Elmshire
• LP47 9XZ, UK
• Telephone: +44 (0)1632 960418
• Fax: +44 (0)1632 960733
• Email: sales@ktfabrications.example
• Web: www.ktfabrications.example
Nice to have
• Nice to have some element of being a British Manufacturer

```html
<!DOCTYPE html>
<html lang="en">
<head>
<meta charset="utf-8">
<title>KT Fabrications Stationery</title>
<link href="https://fonts.googleapis.com/css2?family=Montserrat:wght@500;600&family=Open+Sans:wght@400;600&family=Great+Vibes&display=swap" rel="stylesheet">
<style>
  :root {
    --backdrop: #a87b53;
    --paper: #ffffff;
    --navy: #0356a4;
    --deep: #0b57a6;
    --bright: #0792cd;
    --sky: #33a6d7;
    --pale: #85acd3;
    --ink: #1d1d1b;
    --grey: #6b6b6b;
    --rule: #e3e3e3;
  }
  * { margin: 0; padding: 0; box-sizing: border-box; }
  html, body { width: 1200px; height: 770px; overflow: hidden; }
  body {
    background: var(--backdrop);
    position: relative;
    font-family: "Open Sans", Arial, sans-serif;
    color: var(--ink);
  }
  table { border-collapse: collapse; border-spacing: 0; }
  .sheet {
    position: absolute;
    background: var(--paper);
    box-shadow: 3px 3px 4px rgba(0,0,0,.35);
    overflow: hidden;
  }
  .hazard-band {
    position: absolute; left: 0; right: 0; height: 12px;
    background: repeating-linear-gradient(120deg, var(--ink) 0 30px, var(--bright) 30px 92px);
  }
  .wordmark {
    font-family: "Montserrat", Arial, sans-serif;
    font-weight: 600;
    color: var(--navy);
    letter-spacing: .3em;
    white-space: nowrap;
    display: flex; align-items: center; gap: .5em;
  }
  .wordmark .dot {
    width: .8em; height: .8em; border-radius: 50%;
    background: var(--navy); display: inline-block;
  }

  /* Letterhead */
  .letterhead { left: 62px; top: 79px; width: 488px; height: 634px; }
  .letterhead .wordmark { position: absolute; top: 108px; left: 0; right: 0; justify-content: center; font-size: 15px; }
  .letterhead .hazard-band { top: 569px; }
  .letterhead-footer {
    position: absolute; left: 0; right: 0; top: 581px; bottom: 0;
    background: var(--deep); color: var(--paper);
    font-size: 7.2px; line-height: 11px;
  }
  .letterhead-footer .address { position: absolute; left: 22px; top: 12px; }
  .letterhead-footer .web {
    position: absolute; left: 0; right: 0; top: 28px; text-align: center;
    font-family: "Montserrat", Arial, sans-serif; font-weight: 500; letter-spacing: .08em;
  }
  .letterhead-footer .contact { position: absolute; left: 346px; top: 12px; }
  .contact td { padding: 0; vertical-align: top; line-height: 11px; }
  .contact .label { font-weight: 600; width: 21px; }

  /* Business card */
  .card-front { left: 604px; top: 81px; width: 202px; height: 115px; }
  .card-front .wordmark { position: absolute; left: 16px; top: 30px; font-size: 7px; letter-spacing: .22em; }
  .card-front .top-rule { position: absolute; top: 25px; height: 4px; background: var(--rule); }
  .card-front .person { position: absolute; right: 100px; top: 66px; text-align: right; }
  .person .name { color: var(--bright); font-weight: 600; font-size: 7px; }
  .person .role { color: var(--grey); font-size: 5px; }
  .card-front .divider { position: absolute; left: 111px; top: 50px; width: 1px; height: 44px; background: #cfcfcf; }
  .card-front .details { position: absolute; left: 121px; top: 51px; font-size: 4.6px; line-height: 7.2px; color: var(--grey); }
  .details .lines { margin-bottom: 3px; }
  .details .email { color: var(--navy); }
  .card-front .hazard-band { top: 103px; height: 12px; background: repeating-linear-gradient(120deg, #555 0 22px, var(--bright) 22px 60px); }
  .card-back { left: 826px; top: 81px; width: 203px; height: 115px; background: var(--deep); }
  .card-back .wordmark { position: absolute; inset: 0; justify-content: center; color: var(--paper); font-size: 9px; letter-spacing: .25em; }
  .card-back .wordmark .dot { background: var(--paper); }

  /* Compliments slip */
  .comp-slip { left: 582px; top: 458px; width: 560px; height: 252px; }
  .comp-slip .wordmark { position: absolute; left: 21px; top: 66px; font-size: 10.5px; }
  .comp-slip .greeting {
    position: absolute; right: 28px; top: 22px;
    font-family: "Great Vibes", cursive; font-size: 30px; color: var(--navy);
  }
  .comp-slip .faint-name {
    position: absolute; right: 40px; top: 110px; width: 200px; text-align: center;
    font-family: "Montserrat", Arial, sans-serif; font-weight: 600;
    font-size: 54px; line-height: 1; color: #ececec; letter-spacing: .05em;
  }
  .comp-slip .address { position: absolute; left: 23px; top: 197px; font-size: 7.2px; line-height: 11px; }
  .comp-slip .address strong { font-weight: 600; }
  .comp-slip .divider { position: absolute; left: 142px; top: 197px; width: 1px; height: 30px; background: var(--navy); }
  .comp-slip .contact { position: absolute; left: 157px; top: 197px; font-size: 7.2px; }
  .comp-slip .contact .label { width: 22px; font-weight: 400; }
  .comp-slip .contact .label strong { font-weight: 600; }
  .comp-slip .contact .email { color: var(--navy); font-weight: 600; }
  .comp-slip .hazard-band { top: 234px; height: 18px;
    background: linear-gradient(var(--ink) 0 8px, transparent 8px),
                repeating-linear-gradient(120deg, var(--ink) 0 30px, var(--bright) 30px 92px); }
</style>
</head>
<body>

<section class="sheet letterhead" aria-label="Letterhead">
  <div class="wordmark"><span class="dot"></span>KT FABRICATIONS</div>
  <div class="hazard-band"></div>
  <footer class="letterhead-footer">
    <p class="address">KT Fabrications Limited,<br>Hallmere Road, Marrowby<br>Elmshire, LP47 9XZ, UK</p>
    <p class="web">www.ktfabrications.example</p>
    <table class="contact">
      <tr><td class="label">Tel</td><td>: +44 (0)1632 960418</td></tr>
      <tr><td class="label">Fax</td><td>: +44 (0)1632 960733</td></tr>
      <tr><td class="label">Email</td><td>: sales@ktfabrications.example</td></tr>
    </table>
  </footer>
</section>

<section class="sheet card-front" aria-label="Business card front">
  <div class="top-rule" style="left:0;width:30px"></div>
  <div class="top-rule" style="left:118px;width:84px"></div>
  <div class="wordmark"><span class="dot"></span>KT FABRICATIONS</div>
  <div class="person">
    <p class="name">Your Name Here</p>
    <p class="role">Designation</p>
  </div>
  <div class="divider"></div>
  <div class="details">
    <p class="lines">KT Fabrications Limited,<br>Hallmere Road, Marrowby<br>Elmshire, LP47 9XZ, UK</p>
    <p>&#9990; +44 (0)1632 960418</p>
    <p>&#9632; +44 (0)1632 960733</p>
    <p class="email">&#9993; sales@ktfabrications.example</p>
  </div>
  <div class="hazard-band"></div>
</section>

<section class="sheet card-back" aria-label="Business card back">
  <div class="wordmark"><span class="dot"></span>KT FABRICATIONS</div>
</section>

<section class="sheet comp-slip" aria-label="Compliments slip">
  <div class="wordmark"><span class="dot"></span>KT FABRICATIONS</div>
  <p class="greeting">With Compliments...</p>
  <p class="faint-name" aria-hidden="true">KT</p>
  <p class="address"><strong>KT Fabrications Limited,</strong><br>Hallmere Road, Marrowby<br>Elmshire, LP47 9XZ, UK</p>
  <div class="divider"></div>
  <table class="contact">
    <tr><td class="label"><strong>Tel</strong></td><td>: +44 (0)1632 960418</td></tr>
    <tr><td class="label"><strong>Fax</strong></td><td>: +44 (0)1632 960733</td></tr>
    <tr><td class="label">Email</td><td>: <span class="email">sales@ktfabrications.example</span></td></tr>
  </table>
  <div class="hazard-band"></div>
</section>

</body>
</html>
```